Billboard for a Contractor in Minnesota

Creating our first billboard that will be displayed on a freeway. Will be used on a digital Glint Signboard. Sign should be a 846 x 234 design. Our website is kestrel-paving.com Looking for something specific to "Look us up" or "Call" for your free concrete & asphalt estimate. Needs both web addresses (kestrel-paving.com and kestrel-masonry.com. Needs our phone number, logo. Our slogan is Serving All Your Asphalt & Concrete Needs. It's also our 25 Anniversary.

Target Market(s)

Residential Homeowners in the Twin Cities

Colors
abd036

Requirements
Must have
• Logo, Phone Number, Our Services, Web Addresses (both) Our services are all on our website. (Asphalt Driveway, Concrete Driveway, Concrete Apron, Concrete Sidewalk, Concrete Patio. Colors should be same as website. Black, White, Gray and the Neon Green color.

```html
<!DOCTYPE html>
<html lang="en">
<head>
<meta charset="utf-8">
<title>Kestrel Asphalt &amp; Concrete – Billboard</title>
<link rel="stylesheet" href="https://fonts.googleapis.com/css2?family=Open+Sans:wght@600;700;800&display=swap">
<style>
  :root {
    --canvas: #2a2a2a;
    --neon: #bde83e;
    --neon-shade: #9fc42c;
    --charcoal: #3b3b3b;
    --ink: #2e2e2e;
    --cream: #eef0e2;
    --white: #ffffff;
    --photo-top: #4a4c48;
    --photo-bottom: #2f302e;
  }
  * { margin: 0; padding: 0; box-sizing: border-box; }
  html, body {
    width: 1200px; height: 1200px; overflow: hidden;
    background: var(--canvas);
  }
  .canvas {
    width: 1200px; height: 1200px;
    display: flex; align-items: center; justify-content: center;
  }
  .billboard { display: block; width: 1200px; height: 336px; }
  .billboard text { font-family: "Open Sans", Arial, sans-serif; }
  .slogan { fill: var(--ink); font-weight: 700; font-size: 26px; }
  .offer-free { fill: var(--white); font-weight: 800; font-size: 72px; }
  .offer-sub { fill: var(--white); font-weight: 700; font-size: 32px; }
  .offer-estimate { fill: var(--white); font-weight: 800; font-size: 60px; }
  .service { fill: var(--white); font-weight: 700; font-size: 30px; }
  .web { fill: var(--ink); font-weight: 700; font-size: 20px; }
  .call { fill: var(--white); font-weight: 700; font-size: 34px; }
  .brand-tag { fill: var(--white); font-weight: 600; font-size: 19px; letter-spacing: 1.5px; }
  .brand-name { fill: var(--white); font-weight: 700; font-size: 62px; }
  .anniversary { fill: var(--white); font-weight: 700; font-size: 23px; }
</style>
</head>
<body>
<main class="canvas">
  <svg class="billboard" viewBox="0 0 1500 420" xmlns="http://www.w3.org/2000/svg" aria-label="Kestrel Asphalt &amp; Concrete billboard">
    <defs>
      <linearGradient id="photoTone" x1="0" y1="0" x2="0" y2="1">
        <stop offset="0" stop-color="var(--photo-top)"/>
        <stop offset="1" stop-color="var(--photo-bottom)"/>
      </linearGradient>
    </defs>

    <!-- background -->
    <rect class="bg" width="1500" height="420" fill="var(--neon)"/>

    <!-- house and driveway photo panel -->
    <polygon class="photo-panel" role="img" aria-label="Photo of a house with a freshly paved driveway"
             points="1095,0 1500,0 1500,420 968,420" fill="url(#photoTone)"/>
    <polygon class="photo-corner" points="1330,0 1500,0 1500,68" fill="var(--neon)"/>

    <!-- slogan -->
    <text class="slogan" x="604" y="29" text-anchor="middle">Serving All Your Asphalt &amp; Concrete Needs</text>

    <!-- free estimate card -->
    <g class="offer-card">
      <polygon points="40,58 320,56 420,66 458,330 70,350" fill="var(--neon-shade)"/>
      <polygon points="8,66 437,66 443,382 14,362" fill="var(--cream)"/>
      <polygon points="20,96 406,73 428,354 42,330" fill="var(--charcoal)"/>
      <text class="offer-free" x="230" y="186" text-anchor="middle">FREE</text>
      <text class="offer-sub" x="225" y="228" text-anchor="middle">CONCRETE &amp; ASPHALT</text>
      <text class="offer-estimate" x="242" y="296" text-anchor="middle">ESTIMATE</text>
    </g>

    <!-- services card -->
    <g class="services-card">
      <polygon points="560,72 858,72 890,88 902,312 700,340 545,340" fill="var(--neon-shade)"/>
      <polygon points="548,76 860,74 866,96 540,340" fill="var(--cream)"/>
      <polygon points="570,76 880,88 902,303 540,330" fill="var(--charcoal)"/>
      <text class="service" x="722" y="133" text-anchor="middle">Concrete Patio</text>
      <text class="service" x="722" y="170" text-anchor="middle">Concrete Apron</text>
      <text class="service" x="722" y="206" text-anchor="middle">Asphalt Driveway</text>
      <text class="service" x="722" y="243" text-anchor="middle">Concrete Sidewalk</text>
      <text class="service" x="722" y="279" text-anchor="middle">Concrete Driveway</text>
    </g>

    <!-- web addresses -->
    <text class="web" x="5" y="383">www.kestrel-paving.com</text>
    <text class="web" x="5" y="409">www.kestrel-masonry.com</text>

    <!-- call bar -->
    <g class="call-bar">
      <polygon points="458,352 926,348 930,420 442,420" fill="var(--cream)"/>
      <polygon points="462,362 928,356 936,420 446,420" fill="var(--charcoal)"/>
      <text class="call" x="695" y="409" text-anchor="middle">Call Now 763-555-0148</text>
    </g>

    <!-- brand -->
    <g class="brand">
      <text class="brand-tag" x="1276" y="255" text-anchor="middle">ASPHALT &amp; CONCRETE</text>
      <rect x="1143" y="266" width="265" height="9" fill="var(--white)"/>
      <text class="brand-name" x="1282" y="344" text-anchor="middle">KESTREL</text>
      <text class="anniversary" x="1488" y="409" text-anchor="end">25<tspan font-size="14" dy="-10">th</tspan><tspan dy="10"> Anniversary</tspan></text>
    </g>
  </svg>
</main>
</body>
</html>
```